Harbor Card Design

IT consulting services - my company focuses on delivering value add for clients through sourcing services, strategic and project consulting services, as well as delivering office fitout project managment services.
We also offer IT Interim managment services - to fill the gap when looking for executive roles.
I use orange and blue as my corporate colours
I am after a simple design with my details on the front and my services not the back
Industry/Entity Type
It Company
Contact Information for Business Card
Owen Tredwick
Director
Brightwell Solutions
Owen.Tredwick@BrightwellSolutions.example.au
www.BrightwellSolutions.example.au
m: +61 400582617
On Rear of card:
Interim Management
Project and Strategy Consulting
Sourcing Services
Commercial fit-out management

```html
<!DOCTYPE html>
<html lang="en">
<head>
<meta charset="utf-8">
<title>Harbor Card Design</title>
<link rel="stylesheet" href="https://fonts.googleapis.com/css2?family=Open+Sans:wght@400;600;700&family=Oswald:wght@500&display=swap">
<style>
  :root {
    --navy: #12336b;
    --orange: #f39a12;
    --white: #ffffff;
    --map-tone: #e4e6ea;
    --backdrop: #e9e7e3;
  }
  html, body {
    margin: 0;
    padding: 0;
    overflow: hidden;
  }
  body {
    width: 1200px;
    height: 970px;
    background: var(--backdrop);
    position: relative;
    font-family: "Open Sans", Arial, sans-serif;
  }
  .card {
    position: absolute;
    width: 620px;
    height: 354px;
    box-shadow: 0 10px 28px rgba(0, 0, 0, 0.28);
    background: var(--white);
  }
  .card svg { display: block; }
  .card-back { left: 70px; top: 110px; }
  .card-front { left: 510px; top: 510px; }

  .fill-navy { fill: var(--navy); }
  .fill-white { fill: var(--white); }
  .fill-orange { fill: var(--orange); }

  .brand-name {
    font-family: "Open Sans", Arial, sans-serif;
    font-weight: 700;
    fill: var(--navy);
  }
  .service-item {
    font-family: "Open Sans", Arial, sans-serif;
    font-weight: 600;
    font-size: 13px;
    fill: var(--white);
  }
  .web-address {
    font-family: "Open Sans", Arial, sans-serif;
    font-weight: 600;
    font-size: 13px;
    letter-spacing: 2.5px;
    fill: var(--white);
  }
  .person-name {
    font-family: "Oswald", "Arial Narrow", sans-serif;
    font-weight: 500;
    font-size: 34px;
    fill: var(--white);
  }
  .person-role {
    font-family: "Open Sans", Arial, sans-serif;
    font-weight: 600;
    font-size: 12px;
    letter-spacing: 1.5px;
    fill: var(--white);
  }
  .contact-line {
    font-family: "Open Sans", Arial, sans-serif;
    font-weight: 400;
    font-size: 11px;
    fill: var(--white);
  }
  .contact-icon {
    fill: none;
    stroke: var(--white);
    stroke-width: 1.3;
  }
  .contact-icon-glyph { fill: var(--white); }
</style>
</head>
<body>

  <div class="card card-back">
    <svg width="620" height="354" viewBox="0 0 620 354" xmlns="http://www.w3.org/2000/svg">
      <rect class="fill-white" x="0" y="0" width="620" height="354"/>
      <polygon class="fill-navy" points="430,0 620,0 620,70 560,70"/>
      <polygon class="fill-navy" points="0,205 215,205 232,223 249,205 620,205 620,354 0,354"/>
      <rect class="fill-orange" x="120" y="132" width="30" height="30"/>
      <text class="brand-name" x="162" y="156" font-size="26">Brightwell Solutions</text>

      <g class="service-list">
        <rect class="fill-orange" x="48" y="242" width="7" height="7"/>
        <text class="service-item" x="63" y="250">Interim Management</text>
        <rect class="fill-orange" x="48" y="266" width="7" height="7"/>
        <text class="service-item" x="63" y="274">Project and Strategy Consulting</text>
        <rect class="fill-orange" x="318" y="242" width="7" height="7"/>
        <text class="service-item" x="333" y="250">Sourcing Services</text>
        <rect class="fill-orange" x="318" y="266" width="7" height="7"/>
        <text class="service-item" x="333" y="274">Commercial fit-out management</text>
      </g>

      <text class="web-address" x="48" y="320">www.BrightwellSolutions.example.au</text>
    </svg>
  </div>

  <div class="card card-front">
    <svg width="620" height="354" viewBox="0 0 620 354" xmlns="http://www.w3.org/2000/svg">
      <defs>
        <radialGradient id="map-wash" cx="0.6" cy="0.4" r="0.6">
          <stop offset="0" stop-color="#e4e6ea"/>
          <stop offset="1" stop-color="#ffffff"/>
        </radialGradient>
      </defs>
      <rect class="fill-white" x="0" y="0" width="620" height="354"/>
      <rect x="180" y="0" width="440" height="250" fill="url(#map-wash)" role="img" aria-label="Faint world map in the background"/>

      <rect class="fill-orange" x="36" y="100" width="40" height="40"/>
      <text class="brand-name" x="90" y="135" font-size="38">Brightwell Solutions</text>

      <polygon class="fill-navy" points="0,250 40,250 57,268 74,250 300,250 345,172 620,172 620,354 0,354"/>

      <text class="person-name" x="30" y="308">OWEN TREDWICK</text>
      <text class="person-role" x="32" y="330">DIRECTOR</text>

      <g class="contact-list">
        <circle class="contact-icon" cx="380" cy="198" r="8"/>
        <rect class="contact-icon-glyph" x="377" y="193" width="6" height="10" rx="1.5"/>
        <text class="contact-line" x="396" y="202">+61 400 582 617</text>

        <circle class="contact-icon" cx="380" cy="224" r="8"/>
        <rect class="contact-icon-glyph" x="377" y="219" width="6" height="10" rx="1.5"/>
        <text class="contact-line" x="396" y="228">+61 400 582 618</text>

        <circle class="contact-icon" cx="380" cy="250" r="8"/>
        <rect class="contact-icon-glyph" x="375" y="246" width="10" height="7"/>
        <text class="contact-line" x="396" y="254">owen@brightwellsolutions.example.au</text>

        <circle class="contact-icon" cx="380" cy="276" r="8"/>
        <circle class="contact-icon" cx="380" cy="276" r="4"/>
        <text class="contact-line" x="396" y="280">www.brightwellsolutions.example.au</text>

        <circle class="contact-icon" cx="380" cy="302" r="8"/>
        <path class="contact-icon-glyph" d="M380 308 L376 301 A4 4 0 1 1 384 301 Z"/>
        <text class="contact-line" x="396" y="306">12 Harbour Street, Sydney NSW</text>
      </g>
    </svg>
  </div>

</body>
</html>
```